Mabel's Fitness Business Cards

I would like my business cards to look expensive and sophisticated using my logo and the information below.

FRONT
Mabel’s Fitness logo

Tag line Become your happiest, healthiest and strongest self

Mabel Quint Harlow
Personal Trainer

e. mabel@mabelsfitstudio.example

t. 0781530462

w. www.mabelsfitstudio.example

```html
<!DOCTYPE html>
<html lang="en">
<head>
<meta charset="utf-8">
<title>Mabel's Fitness Business Cards</title>
<link rel="stylesheet" href="https://fonts.googleapis.com/css2?family=Montserrat:wght@300;400;500&display=swap">
<style>
  :root {
    --backdrop: #1b1b1b;
    --card: #0b0b0c;
    --teal: #7cc4d0;
    --teal-bright: #25b4e6;
    --taupe: #b9aaa8;
    --text-light: #e9e9e9;
    --ring-grey: #3a3a3d;
    --disc: #f4f4f4;
  }
  * { margin: 0; padding: 0; box-sizing: border-box; }
  html, body { width: 1200px; height: 864px; overflow: hidden; }
  body {
    background: radial-gradient(ellipse at 50% 45%, #262626 0%, var(--backdrop) 70%);
    font-family: "Montserrat", sans-serif;
    position: relative;
  }
  .card {
    position: absolute;
    width: 504px;
    height: 288px;
    background: var(--card);
    border-radius: 6px;
    box-shadow: 0 18px 40px rgba(0,0,0,0.6);
    overflow: hidden;
  }
  /* Brand side */
  .card--brand { left: 600px; top: 130px; }
  .brand-ring {
    position: absolute;
    left: 40px; top: 34px;
    width: 220px; height: 220px;
    border-radius: 50%;
    border: 6px solid var(--ring-grey);
  }
  .brand-name {
    position: absolute;
    left: 282px; top: 98px;
    color: var(--teal);
    font-weight: 400;
    font-size: 30px;
    letter-spacing: 2px;
    text-transform: uppercase;
    line-height: 1.1;
  }
  .tagline {
    position: absolute;
    left: 282px; top: 186px;
    width: 200px;
    color: var(--text-light);
    font-size: 10px;
    letter-spacing: 1.5px;
    line-height: 1.6;
    text-transform: uppercase;
  }
  /* Contact side */
  .card--contact { left: 96px; top: 446px; }
  .contact-disc {
    position: absolute;
    left: 30px; top: 52px;
    width: 184px; height: 184px;
    border-radius: 50%;
    background: var(--disc);
    box-shadow: 0 0 0 5px var(--card), 0 0 0 8px var(--teal-bright);
    display: flex; align-items: center; justify-content: center;
  }
  .disc-name {
    color: var(--teal);
    font-size: 17px;
    font-weight: 400;
    letter-spacing: 1.5px;
    text-transform: uppercase;
    text-align: center;
    line-height: 1.25;
  }
  .details {
    position: absolute;
    left: 240px; top: 76px;
    color: var(--text-light);
  }
  .person-name {
    color: var(--teal);
    font-size: 17px;
    font-weight: 400;
    letter-spacing: 1px;
    text-transform: uppercase;
  }
  .person-role {
    font-size: 12px;
    font-weight: 300;
    margin-bottom: 14px;
  }
  .contact-list { list-style: none; }
  .contact-item {
    display: flex; align-items: center; gap: 8px;
    font-size: 13px;
    font-weight: 300;
    margin-bottom: 6px;
  }
  .contact-item svg { width: 14px; height: 14px; flex: none; }
  .web strong { font-weight: 500; color: var(--teal); }
</style>
</head>
<body>

<section class="card card--brand" aria-label="Business card, brand side">
  <div class="brand-ring"></div>
  <div class="brand-name">Mabel’s<br>Fitness</div>
  <p class="tagline">Become your happiest, healthiest and strongest self</p>
</section>

<section class="card card--contact" aria-label="Business card, contact side">
  <div class="contact-disc">
    <div class="disc-name">Mabel’s<br>Fitness</div>
  </div>
  <div class="details">
    <h1 class="person-name">Mabel Quint Harlow</h1>
    <p class="person-role">Personal Trainer</p>
    <ul class="contact-list">
      <li class="contact-item">
        <svg viewBox="0 0 14 14" fill="none" stroke="#e9e9e9" stroke-width="1.2"><circle cx="7" cy="7" r="6.2"/><path d="M4.6 4.2c.5-.5 1-.4 1.3.1l.5.9c.2.4 0 .7-.3 1 .4.8.9 1.3 1.7 1.7.3-.3.6-.5 1-.3l.9.5c.5.3.6.8.1 1.3-1.6 1.4-6.5-3.4-5.2-5.2z" fill="#e9e9e9" stroke="none"/></svg>
        078 1530 462
      </li>
      <li class="contact-item">
        <svg viewBox="0 0 14 14" fill="none" stroke="#e9e9e9" stroke-width="1.2"><circle cx="7" cy="7" r="6.2"/><rect x="3.8" y="4.8" width="6.4" height="4.4" rx=".5"/><path d="M3.8 5l3.2 2.3L10.2 5"/></svg>
        mabel@mabelsfitstudio.example
      </li>
      <li class="contact-item web">
        <svg viewBox="0 0 14 14" fill="none" stroke="#e9e9e9" stroke-width="1.1"><circle cx="7" cy="7" r="6.2"/><circle cx="7" cy="7" r="3.6"/><path d="M3.4 7h7.2M7 3.4c-1.4 2.2-1.4 5 0 7.2M7 3.4c1.4 2.2 1.4 5 0 7.2"/></svg>
        <span>www.<strong>mabelsfitstudio</strong>.example</span>
      </li>
    </ul>
  </div>
</section>

</body>
</html>
```